Kestrel Chiropractic Clinic Design

I am a Chiropractor and I treat a lot of conditions ranging from aches and pains to arthritis and nervous system issues. I would like a professional looking card with my logo and all of the other information that I have provided up top. I do like working with athletes (runners, football players, crossfit, and sports of that nature) so that is one aspect of my practice that varies from some of the others in town. My goal is to get patients out of pain and back to living their lives and doing what they love.

I would like to have a grey background also. Most of my marketing banners and things have the logo on a grey background and I would like to stick with that if possible.
Updates

Hello Everyone,

So one of the things that I wanted was a Grey background for the logo. All of my other marketing things have the logo on a grey background (pantone color 428C). If I could get that color on both the front and the back of the card I would appreciate it. I don't care if the card has white on it I just want my logo sitting on the grey color if possible.

Target Market(s)

really just everyone with emphasis on Athletes ranging from 18-35 years old

Industry/Entity Type

Marketing

Contact Information for Business Card

Kestrel Chiropractic Clinic
Dr. Wesley Marlow
4718 Hollow Brook, Suite 300
Cedar Bluff, KS 66012
phone= 555-812-3961
fax= 555-812-7045
email= kestrelchiroclinic@mailbox.example

Requirements
Must have
• I must have my logo present

```html
<!DOCTYPE html>
<html lang="en">
<head>
<meta charset="utf-8">
<title>Kestrel Chiropractic Clinic – Business Card</title>
<link rel="stylesheet" href="https://fonts.googleapis.com/css2?family=Lato:wght@400;700&family=Libre+Baskerville:wght@400;700&display=swap">
<style>
  :root {
    --page-bg: #d9d9db;
    --card-light: #f4f4f5;
    --card-grey: #dcdcde;
    --panel-dark: #2e2f31;
    --panel-mid: #4a4b4e;
    --brand-blue: #2448d8;
    --brand-green: #5ad43a;
    --figure-tone: #b9c3d6;
    --figure-green: #c9dcc4;
    --text-light: #f2f2f2;
  }
  * { margin: 0; padding: 0; box-sizing: border-box; }
  html, body { width: 1200px; height: 800px; overflow: hidden; }
  body {
    background: var(--page-bg);
    display: flex;
    align-items: center;
    justify-content: center;
    gap: 40px;
  }
  .card {
    position: relative;
    width: 540px;
    height: 308px;
    overflow: hidden;
    box-shadow: 0 6px 18px rgba(0,0,0,0.25);
    background: radial-gradient(ellipse at 45% 40%, var(--card-light), var(--card-grey));
  }
  .card-art { position: absolute; inset: 0; width: 100%; height: 100%; }
  .wordmark {
    position: absolute;
    display: flex;
    align-items: center;
    gap: 10px;
    font-family: "Lato", sans-serif;
    font-weight: 700;
    color: var(--brand-blue);
    white-space: nowrap;
  }
  .wordmark-dot {
    border-radius: 50%;
    background: var(--brand-blue);
    flex: none;
  }
  .card-front .wordmark { left: 50%; top: 92px; transform: translateX(-50%); font-size: 30px; }
  .card-front .wordmark-dot { width: 18px; height: 18px; }
  .card-back .wordmark { left: 138px; top: 36px; font-size: 15px; }
  .card-back .wordmark-dot { width: 10px; height: 10px; }
  .contact {
    position: absolute;
    left: 0; right: 0;
    top: 148px;
    text-align: center;
    font-family: "Libre Baskerville", serif;
    color: var(--text-light);
  }
  .contact-name { font-size: 19px; font-weight: 700; margin-bottom: 16px; }
  .contact-lines { font-size: 10.5px; line-height: 1.55; font-weight: 700; }
</style>
</head>
<body>

  <section class="card card-front" aria-label="Card front">
    <svg class="card-art" viewBox="0 0 540 308" preserveAspectRatio="none">
      <path d="M280 0 H540 V86 C470 40 390 12 280 0 Z" fill="var(--brand-blue)"/>
      <path d="M280 0 C390 12 470 40 540 86" fill="none" stroke="var(--brand-green)" stroke-width="5"/>
      <rect role="img" aria-label="Faint silhouettes of a group of people" x="360" y="170" width="170" height="130" rx="12" fill="var(--figure-tone)" opacity="0.45"/>
      <path d="M0 196 C60 250 170 292 300 308 H0 Z" fill="var(--brand-blue)"/>
      <path d="M0 186 C64 244 176 288 310 308" fill="none" stroke="var(--brand-green)" stroke-width="5"/>
    </svg>
    <div class="wordmark"><span class="wordmark-dot"></span>Kestrel Chiropractic Clinic</div>
  </section>

  <section class="card card-back" aria-label="Card back">
    <svg class="card-art" viewBox="0 0 540 308" preserveAspectRatio="none">
      <defs>
        <radialGradient id="panel-shade" cx="50%" cy="40%" r="70%">
          <stop offset="0" stop-color="var(--panel-mid)"/>
          <stop offset="1" stop-color="var(--panel-dark)"/>
        </radialGradient>
      </defs>
      <rect role="img" aria-label="Faint silhouettes of athletes" x="8" y="12" width="110" height="100" rx="10" fill="var(--figure-green)" opacity="0.6"/>
      <rect role="img" aria-label="Faint silhouettes of a group of people" x="400" y="30" width="130" height="90" rx="10" fill="var(--figure-tone)" opacity="0.5"/>
      <path d="M330 0 H540 V52 C480 22 410 6 330 0 Z" fill="var(--brand-blue)"/>
      <path d="M330 0 C410 6 480 22 540 52" fill="none" stroke="var(--brand-green)" stroke-width="4"/>
      <rect x="0" y="118" width="540" height="190" fill="url(#panel-shade)"/>
      <path d="M0 210 C60 262 170 296 300 308 H0 Z" fill="var(--brand-blue)"/>
      <path d="M0 200 C64 256 176 292 310 308" fill="none" stroke="var(--brand-green)" stroke-width="4"/>
    </svg>
    <div class="wordmark"><span class="wordmark-dot"></span>Kestrel Chiropractic Clinic</div>
    <div class="contact">
      <p class="contact-name">Dr. Wesley Marlow</p>
      <div class="contact-lines">
        <p>4718 Hollow Brook, Suite 300 Cedar Bluff, KS 66012</p>
        <p>Phone - 555-812-3961</p>
        <p>Fax - 555-812-7045</p>
        <p>Email - kestrelchiroclinic@mailbox.example</p>
      </div>
    </div>
  </section>

</body>
</html>
```